Creative way to lay out a career advancement graphic

Are you a designer with a knack for turning complex concepts into visually captivating masterpieces? We have an exciting project that needs your unique talent! We're on the lookout for a creative designer to help us visualize our company's diverse career paths. Our organization offers a plethora of opportunities in project management, engineering, sales, and more. We want to showcase these pathways in a visually engaging manner to empower potential job candidates with a clear understanding of their advancement options within our company. Design must be flexible and able to be edited.

Check out the attached examples of the positions we'd like to include in this visualization (doc "inside sales" are correct positions). Your task will be to transform this information into a visually stunning representation that's both informative and inspiring.
This project is not just about design—it's about shaping the narrative of career growth and opportunity within our organization. Your creative input will play a vital role in helping us attract top talent and communicate our company's commitment to fostering professional development. Brand guidelines are also attached for reference. The document titled "quarbel" demonstrates a badly done version of what we are trying to achieve. We want to denote multiple routes of advancement. You don't have to get the paths completely correct, you just need to show how it could be approached in a design. For example, A "submittal Specialist" could become a "project manager" but also could ascend to the role of "Industrial Estimator" if they want to move in that direction.

```html
<!DOCTYPE html>
<html lang="en">
<head>
<meta charset="utf-8">
<title>Norvale Career Paths</title>
<link rel="stylesheet" href="https://fonts.googleapis.com/css2?family=Poppins:wght@300;400;500;600;700;800&display=swap">
<style>
  :root {
    --orange: #f5a51e;
    --ink: #0d0d0d;
    --paper: #ffffff;
    --muted: #7a7a7a;
    --map: #ececec;
  }
  * { box-sizing: border-box; margin: 0; padding: 0; }
  html, body { width: 800px; height: 1200px; overflow: hidden; background: var(--paper); }
  body { font-family: "Poppins", sans-serif; color: var(--ink); }
  .canvas { position: relative; width: 800px; height: 1200px; overflow: hidden; background: var(--paper); }

  .map-band { position: absolute; left: 7px; width: 775px; border-radius: 40px;
    background: radial-gradient(ellipse at center, rgba(225,225,225,.55), rgba(255,255,255,0) 70%); }
  .map-band--upper { top: 174px; height: 323px; }
  .map-band--lower { top: 856px; height: 219px; }

  .brand { position: absolute; left: 42px; top: 52px; }
  .brand-name { display: flex; align-items: center; gap: 7px; font-size: 31px; font-weight: 800; letter-spacing: 0.5px; line-height: 1; color: var(--ink); }
  .brand-dot { width: 16px; height: 16px; border-radius: 50%; background: var(--orange); }
  .brand-tagline { margin-top: 5px; font-size: 8.4px; font-weight: 400; letter-spacing: 2.1px; color: var(--muted); }

  .paths { position: absolute; inset: 0; width: 800px; height: 1200px; }
  .paths path { fill: none; stroke: var(--ink); stroke-width: 3.6; stroke-linecap: round; }

  .avatar { position: absolute; width: 62px; height: 62px; border-radius: 50%; background: var(--paper);
    box-shadow: 0 2px 6px rgba(0,0,0,.28); }
  .avatar::before { content: ""; position: absolute; inset: 5px; border-radius: 50%; border: 5px solid var(--ring); }
  .avatar-mark { position: absolute; left: 20px; top: 20px; width: 22px; height: 22px; border-radius: 50%; background: var(--ring); }
  .avatar--dark { --ring: var(--ink); }
  .avatar--orange { --ring: var(--orange); }

  .role { position: absolute; width: 222px; padding: 0 6px 5px; background: var(--paper); border-radius: 14px;
    box-shadow: 0 3px 7px rgba(0,0,0,.22); }
  .role-title { height: 21px; line-height: 22px; text-align: center; font-size: 11px; font-weight: 700; letter-spacing: 0.1px; white-space: nowrap; }
  .role-title .light { font-weight: 400; }
  .role-title--stacked { height: 25px; line-height: 10.5px; padding-top: 3px; }
  .role-duties { list-style: none; border-radius: 12px; padding: 6px 8px 4px 10px; font-size: 8.4px; line-height: 10.4px; font-weight: 500; }
  .role-duties li { position: relative; padding-left: 9px; margin-bottom: 2.2px; }
  .role-duties li::before { content: ""; position: absolute; left: 0; top: 3.3px; width: 4.2px; height: 4.2px; border-radius: 50%; background: var(--dot); }
  .role-duties--orange { background: var(--orange); color: var(--ink); --dot: var(--ink); }
  .role-duties--dark { background: var(--ink); color: var(--paper); --dot: var(--orange); }
  .role-duties--dense li { margin-bottom: 0.6px; line-height: 9.8px; }
</style>
</head>
<body>
<main class="canvas">
  <div class="map-band map-band--upper" role="img" aria-label="Faint world map backdrop"></div>
  <div class="map-band map-band--lower" role="img" aria-label="Faint world map backdrop"></div>

  <header class="brand">
    <div class="brand-name"><span class="brand-dot"></span>NORVALE</div>
    <div class="brand-tagline">The Energy Solutions Company</div>
  </header>

  <svg class="paths" viewBox="0 0 800 1200" aria-hidden="true">
    <defs>
      <marker id="arrowhead" viewBox="0 0 10 10" refX="6" refY="5" markerWidth="18" markerHeight="18" markerUnits="userSpaceOnUse" orient="auto">
        <path d="M0,0 L10,5 L0,10 L3,5 Z" style="fill:#0d0d0d;stroke:none"/>
      </marker>
    </defs>
    <path d="M279,276 Q225,230 272,152" marker-end="url(#arrowhead)"/>
    <path d="M520,440 Q572,395 540,320" marker-end="url(#arrowhead)"/>
    <path d="M169,521 Q195,455 270,436" marker-end="url(#arrowhead)"/>
    <path d="M336,552 L222,553" marker-end="url(#arrowhead)"/>
    <path d="M584,552 L468,553" marker-end="url(#arrowhead)"/>
    <path d="M215,724 L330,725" marker-end="url(#arrowhead)"/>
    <path d="M454,724 L570,725" marker-end="url(#arrowhead)"/>
    <path d="M690,749 Q760,760 758,690" marker-end="url(#arrowhead)"/>
    <path d="M172,1081 Q118,1010 146,893" marker-end="url(#arrowhead)"/>
    <path d="M197,1078 Q170,995 272,973" marker-end="url(#arrowhead)"/>
    <path d="M473,1051 L346,1052" marker-end="url(#arrowhead)"/>
  </svg>

  <!-- Vice President -->
  <div class="avatar avatar--dark" style="left:368px;top:28px"><span class="avatar-mark" role="img" aria-label="Person icon"></span></div>
  <section class="role" style="left:288px;top:93px">
    <h2 class="role-title">VICE PRESIDENT , <span class="light">SALES</span></h2>
    <ul class="role-duties role-duties--orange" style="height:64px">
      <li>Sales strategy development</li>
      <li>Revenue generation</li>
      <li>Market analysis</li>
      <li>Sales forecasting and budgeting</li>
      <li>Team Leadership</li>
    </ul>
  </section>

  <!-- Sales Leadership -->
  <div class="avatar avatar--orange" style="left:368px;top:195px"><span class="avatar-mark" role="img" aria-label="Person icon"></span></div>
  <section class="role" style="left:288px;top:258px">
    <h2 class="role-title">SALES LEADERSHIP</h2>
    <ul class="role-duties role-duties--dark" style="height:64px">
      <li>Sets sets goals and targets</li>
      <li>Sales team supervision, mentoring, training and coaching</li>
      <li>Sales strategy development and implementation</li>
    </ul>
  </section>

  <!-- Outside Sales -->
  <div class="avatar avatar--dark" style="left:368px;top:357px"><span class="avatar-mark" role="img" aria-label="Person icon"></span></div>
  <section class="role" style="left:288px;top:421px">
    <h2 class="role-title">OUTSIDE SALES</h2>
    <ul class="role-duties role-duties--orange" style="height:65px;padding-top:9px">
      <li>Prospecting and lead generation</li>
      <li>Building and maintaining relationships</li>
      <li>Closing sales and achieving targets</li>
    </ul>
  </section>

  <!-- Lead row -->
  <div class="avatar avatar--dark" style="left:124px;top:521px"><span class="avatar-mark" role="img" aria-label="Person icon"></span></div>
  <section class="role" style="left:44px;top:585px">
    <h2 class="role-title">LEAD PROJECT MANAGER</h2>
    <ul class="role-duties role-duties--orange" style="height:73px">
      <li>Team leadership, mentoring &amp; training</li>
      <li>Project planning &amp; organiztion Monitoring and control</li>
      <li>Customer service and communication</li>
      <li>Continuous improvement</li>
    </ul>
  </section>

  <div class="avatar avatar--orange" style="left:368px;top:521px"><span class="avatar-mark" role="img" aria-label="Person icon"></span></div>
  <section class="role" style="left:288px;top:585px">
    <h2 class="role-title">LEAD TECHNICAL ENGINEER</h2>
    <ul class="role-duties role-duties--dark" style="height:73px">
      <li>Team leadership, mentoring and training</li>
      <li>Technical sales liaison</li>
      <li>Influence specifications</li>
      <li>Read &amp; interpret specifications</li>
    </ul>
  </section>

  <div class="avatar avatar--dark" style="left:609px;top:521px"><span class="avatar-mark" role="img" aria-label="Person icon"></span></div>
  <section class="role" style="left:529px;top:585px">
    <h2 class="role-title">LEAD PROJECT ENGINEER</h2>
    <ul class="role-duties role-duties--orange role-duties--dense" style="height:73px;padding-top:3px;font-size:8.1px">
      <li>Team leadership, mentoring &amp; training</li>
      <li>Technical expertise, engineering support</li>
      <li>Subject matter expert relating to job, equipment and commissioning</li>
      <li>Quality control and project execution</li>
      <li>Continuous improvement</li>
    </ul>
  </section>

  <!-- Core row -->
  <div class="avatar avatar--orange" style="left:124px;top:693px"><span class="avatar-mark" role="img" aria-label="Person icon"></span></div>
  <section class="role" style="left:44px;top:757px">
    <h2 class="role-title">PROJECT MANAGER</h2>
    <ul class="role-duties role-duties--dark" style="height:64px">
      <li>Project planning and organization</li>
      <li>Monitoring and control</li>
      <li>Customer service &amp; communication</li>
    </ul>
  </section>

  <div class="avatar avatar--dark" style="left:368px;top:693px"><span class="avatar-mark" role="img" aria-label="Person icon"></span></div>
  <section class="role" style="left:288px;top:757px">
    <h2 class="role-title">INDUSTRIAL ESTIMATOR<span class="light">(SENIOR)</span></h2>
    <ul class="role-duties role-duties--orange" style="height:64px;padding-top:4px">
      <li>Quote preparation for complex jobs</li>
      <li>Specification and drawing review</li>
      <li>Customer and vendor relationship</li>
      <li>Analyze competitive pricing</li>
      <li>Support outside sales</li>
    </ul>
  </section>

  <div class="avatar avatar--orange" style="left:609px;top:693px"><span class="avatar-mark" role="img" aria-label="Person icon"></span></div>
  <section class="role" style="left:529px;top:757px">
    <h2 class="role-title">PROJECT ENGINEER</h2>
    <ul class="role-duties role-duties--dark" style="height:64px">
      <li>Technical expertise + engineering Support</li>
      <li>Subject matter expert relating to job, equipment and commissioning</li>
      <li>Quality control and project execution</li>
    </ul>
  </section>

  <!-- Estimator -->
  <div class="avatar avatar--dark" style="left:368px;top:859px"><span class="avatar-mark" role="img" aria-label="Person icon"></span></div>
  <section class="role" style="left:288px;top:923px">
    <h2 class="role-title">INDUSTRIAL ESTIMATOR<span class="light">(SENIOR)</span></h2>
    <ul class="role-duties role-duties--orange" style="height:66px">
      <li>Quote preparation for less complex jobs</li>
      <li>Specification and drawing Review</li>
      <li>Vendor relationship</li>
      <li>Support outside sales</li>
    </ul>
  </section>

  <!-- Entry row -->
  <div class="avatar avatar--dark" style="left:250px;top:1020px"><span class="avatar-mark" role="img" aria-label="Person icon"></span></div>
  <section class="role" style="left:170px;top:1083px">
    <h2 class="role-title" style="height:25px;line-height:28px">SUBMITTAL SPECIALIST</h2>
    <ul class="role-duties role-duties--orange" style="height:64px;padding-top:8px">
      <li>Document control and management</li>
      <li>Submittal preparation and review</li>
      <li>Communication and coordination</li>
    </ul>
  </section>

  <div class="avatar avatar--orange" style="left:495px;top:1020px"><span class="avatar-mark" role="img" aria-label="Person icon"></span></div>
  <section class="role" style="left:415px;top:1083px">
    <h2 class="role-title role-title--stacked">PROJECT COORDINATOR<br><span class="light">(GATEKEEPER)</span></h2>
    <ul class="role-duties role-duties--dark" style="height:64px;padding-top:8px">
      <li>Data entry for projects</li>
      <li>Reviews project complexity &amp; assigns accordingly</li>
    </ul>
  </section>
</main>
</body>
</html>
```